Business Card Design Project

Hi Designers, this project is currently on hold until the Logo is completed:
Please submit to the Logo project here:
http://jobs.pixelmarket.example/job.aspx?id=371905

Once logo is completed, it will be attached to this project for you to create business cards with show logo, company name and address

Maren T K Ashdown

Corwin's Meadow Pine Flock Co.
Hazelmere
Upper Brackwell
North Devon EX21 4TN

Tel: 01809 351846
Mobile: 07912 463078
email: maren@meadow-pine-flock.example
Updates

Project Deadline Extended
Reason: Sorry everyone, we have had a sick ewe and I am now behind with this one and need to extend the deadline. Best wishes Maren

The designer who wins the logo brief will be asked to design the business card. Many thanks Maren

Project Deadline Extended
Reason: Sorry everyone, just a chaotic time of year with animals. Need to extend the deadline again..... as I just haven't had enough time to take a good look.... Thank you for your understanding. Maren

Project Deadline Extended
Reason: Sorry everyone It is our busiest time of year with animals and just no time to spend going through such great designs. I will have to extend the deadline again and hopefully have some news very soon. Wishing you all a very happy Christmas and a happy and healthy new year. Maren & Corwin

Target Market(s)

High end market
Boutique restaurants for meat (it's not commercial lamb it's a slow matured quality meat more like venison/beef) expensive - specialized market

High End shoot clothing / wool / sheepskin rugs
Quality products

Industry/Entity Type

Business

Requirements
Must have
• based on the logo - (which Pixel Market has just been asked to do)
possibly based on a simplified picture of a Hebridean Ram (shows it's a Hebridean by it's horns as opposed to other black sheep!!)

```html
<!DOCTYPE html>
<html lang="en">
<head>
<meta charset="utf-8">
<title>Corwin's Meadow Pine Flock Co. – Business Cards</title>
<link href="https://fonts.googleapis.com/css2?family=Ubuntu:wght@400;500&display=swap" rel="stylesheet">
<style>
  :root {
    --page: #e6e3e0;
    --card: #3a2221;
    --card-edge: #2c1817;
    --teal: #2bb5b2;
    --ink: #170d0c;
    --text-dark: #1e1110;
  }
  html, body {
    margin: 0;
    padding: 0;
    width: 1200px;
    height: 873px;
    overflow: hidden;
    background: var(--page);
  }
  .canvas {
    position: relative;
    width: 1200px;
    height: 873px;
    display: flex;
    align-items: center;
    justify-content: center;
    gap: 60px;
    font-family: "Ubuntu", sans-serif;
  }
  .card {
    position: relative;
    width: 520px;
    height: 336px;
    background: var(--card);
    border-radius: 4px;
    box-shadow: 0 10px 24px rgba(0,0,0,.22);
    overflow: hidden;
  }
  .card--back {
    background: linear-gradient(135deg, #452a28 0%, var(--card) 45%, var(--card-edge) 100%);
  }

  /* Brand mark stand-in: name plus one plain circle */
  .brand {
    display: flex;
    align-items: center;
    gap: 14px;
    color: var(--teal);
    font-weight: 400;
  }
  .brand__dot {
    flex: none;
    border-radius: 50%;
    background: var(--teal);
  }
  .card--front .brand {
    position: absolute;
    inset: 0;
    flex-direction: column;
    justify-content: center;
    font-size: 26px;
    gap: 22px;
  }
  .card--front .brand__dot { width: 110px; height: 110px; }

  .card--back .brand {
    position: absolute;
    left: 34px;
    top: 40px;
    width: 210px;
    flex-direction: column;
    font-size: 15px;
    gap: 14px;
    text-align: center;
  }
  .card--back .brand__dot { width: 64px; height: 64px; }

  .contact {
    position: absolute;
    left: 270px;
    top: 150px;
    color: var(--text-dark);
  }
  .contact__name {
    margin: 0 0 14px;
    font-size: 20px;
    font-weight: 500;
    color: var(--ink);
  }
  .contact__list {
    list-style: none;
    margin: 0;
    padding: 0;
    font-size: 12.5px;
    line-height: 1.45;
  }
  .contact__item {
    display: flex;
    align-items: flex-start;
    gap: 9px;
    margin-bottom: 4px;
  }
  .contact__icon {
    flex: none;
    width: 14px;
    height: 14px;
    margin-top: 2px;
  }
</style>
</head>
<body>
<main class="canvas">

  <section class="card card--back" aria-label="Business card, contact side">
    <div class="brand">
      <span class="brand__dot"></span>
      <span class="brand__name">Corwin's Meadow Pine Flock Co.</span>
    </div>

    <div class="contact">
      <h1 class="contact__name">Maren T K Ashdown</h1>
      <ul class="contact__list">
        <li class="contact__item">
          <svg class="contact__icon" viewBox="0 0 14 14" aria-hidden="true">
            <rect width="14" height="14" rx="2" fill="var(--teal)"/>
            <path d="M4 3.2l1.6 0 .7 2-1 .8a6 6 0 0 0 2.7 2.7l.8-1 2 .7v1.6A1.2 1.2 0 0 1 9.6 11 7 7 0 0 1 3 4.4 1.2 1.2 0 0 1 4 3.2z" fill="var(--card)"/>
          </svg>
          <span>01809 351846</span>
        </li>
        <li class="contact__item">
          <svg class="contact__icon" viewBox="0 0 14 14" aria-hidden="true">
            <rect width="14" height="14" rx="2" fill="var(--teal)"/>
            <rect x="4.5" y="2.5" width="5" height="9" rx="1" fill="var(--card)"/>
            <rect x="5.3" y="3.5" width="3.4" height="5.5" fill="var(--teal)"/>
          </svg>
          <span>07912 463078</span>
        </li>
        <li class="contact__item">
          <svg class="contact__icon" viewBox="0 0 14 14" aria-hidden="true">
            <rect width="14" height="14" rx="2" fill="var(--teal)"/>
            <rect x="2.5" y="4" width="9" height="6" fill="var(--card)"/>
            <path d="M2.5 4l4.5 3.4L11.5 4" fill="none" stroke="var(--teal)" stroke-width="1"/>
          </svg>
          <span>maren@meadow-pine-flock.example</span>
        </li>
        <li class="contact__item">
          <svg class="contact__icon" viewBox="0 0 14 14" aria-hidden="true">
            <rect width="14" height="14" rx="2" fill="var(--teal)"/>
            <path d="M7 2.5a3 3 0 0 1 3 3c0 2.2-3 6-3 6s-3-3.8-3-6a3 3 0 0 1 3-3z" fill="var(--card)"/>
            <circle cx="7" cy="5.5" r="1.1" fill="var(--teal)"/>
          </svg>
          <span>Hazelmere<br>Upper Brackwell<br>North Devon EX21 4TN</span>
        </li>
      </ul>
    </div>
  </section>

  <section class="card card--front" aria-label="Business card, brand side">
    <div class="brand">
      <span class="brand__dot"></span>
      <span class="brand__name">Corwin's Meadow Pine Flock Co.</span>
    </div>
  </section>

</main>
</body>
</html>
```